Startup online payment business - Sporting / Golf, Fairway Tally payment

Background:
Our business name is "Fairway Tally" we provide online payments for golfing services via our website. We currently have a logo used on our website. No other design style has been developed. Our aim is to remove cash payments for service at golf clubs.

Our Key Values:
Quick and easy
Formal and polite
Fun with professional boundary
Mate-ship relationships
100% online digital

What we want from you:
Marketing design to be used on posters and stickers in a retail setting to direct customers to our online payment Chanel.
Design must incorporate attached logo, URL fairwaytally.com.au and our key values can act as a guide the type of design. We have used color Hex#007672 for logo background. We are open to use other colors.

Target Market(s)

Golf clubs and golf players

Industry/Entity Type

Golf Course

Font styles to use
Sans Serif

Requirements
Must have
• Directions to online payment via URL: fairwaytally.com.au
Nice to have
• We like the idea of the slogan: No Cash - No worries. Have attached home screen that will be available from URL link. Consideration if using mobile phone in image. Push the online payment and steps 1. Visit fairwaytally.com 2. Select club 3. Confirm payment
Should not have
• Cartoons

```html
<!DOCTYPE html>
<html lang="en">
<head>
<meta charset="utf-8">
<title>Fairway Tally Poster</title>
<link rel="stylesheet" href="https://fonts.googleapis.com/css2?family=Source+Sans+3:ital,wght@0,400;0,600;0,700;1,700&display=swap">
<style>
  :root {
    --backdrop: #c4f5d2;
    --teal: #0b7470;
    --teal-deep: #0a5f5b;
    --teal-top: #166b67;
    --leaf: #7aa23a;
    --white: #ffffff;
    --paper: #f1f3f2;
    --ink-teal: #0d6f6b;
    --pill-text: #e3eeec;
  }
  * { box-sizing: border-box; margin: 0; padding: 0; }
  html, body {
    width: 1200px; height: 1200px; overflow: hidden;
    background: var(--backdrop);
    font-family: "Source Sans 3", "Helvetica Neue", Arial, sans-serif;
  }
  .poster {
    position: absolute; left: 241px; top: 100px;
    width: 718px; height: 1000px; overflow: hidden;
    background: linear-gradient(180deg, var(--teal-top) 0 339px, var(--teal) 339px 100%);
  }
  .poster > * { position: absolute; }
  .hero-photo {
    left: 25px; top: 23px; width: 668px; height: 370px;
    background:
      radial-gradient(ellipse at 40% 20%, #f3ec9a 0%, rgba(243,236,154,0) 55%),
      linear-gradient(180deg, #d8d873 0%, #a9c24c 35%, #6f9d2a 65%, #4f8a1e 100%);
  }
  .frame { left: 0; top: 0; width: 718px; height: 1000px; }
  .brand-tab { left: 31px; top: 0; width: 207px; height: 161px; }
  .brand-name {
    left: 31px; top: 58px; width: 207px; text-align: center;
    color: var(--white); font-weight: 600; font-size: 31px; letter-spacing: 0.5px;
  }
  .values-title {
    left: 115px; top: 406px; color: var(--white);
    font-weight: 700; font-size: 25px;
  }
  .values-list { left: 80px; top: 468px; list-style: none; }
  .values-list li {
    display: flex; align-items: center; height: 25px;
    color: var(--white); font-size: 17px;
  }
  .values-list li::before {
    content: ""; width: 0; height: 0; margin-right: 22px;
    border-left: 13px solid #d9e6e4;
    border-top: 7px solid transparent; border-bottom: 7px solid transparent;
  }
  .offer-panel { left: 368px; top: 417px; width: 350px; height: 179px; }
  .offer-text {
    right: 71px; top: 445px; text-align: right;
    color: var(--white); font-weight: 600; font-size: 22px; line-height: 30.5px;
  }
  .steps-panel { left: 6px; top: 626px; width: 712px; height: 187px; }
  .phone-mockup {
    left: 78px; top: 630px; width: 86px; height: 178px;
    border-radius: 12px; border: 2px solid #cfd3d4;
    background: linear-gradient(180deg, #f7f7f7 0 12%, #0e7470 12% 88%, #f7f7f7 88%);
  }
  .steps-title {
    left: 200px; top: 655px; color: var(--ink-teal);
    font-weight: 700; font-size: 22px; text-decoration: underline; text-underline-offset: 3px;
  }
  .steps-list { left: 202px; top: 701px; list-style: none; color: var(--ink-teal); font-size: 17px; }
  .steps-list li { height: 34px; display: flex; }
  .steps-list .num { width: 29px; }
  .url-pill {
    left: 161px; top: 841px; width: 402px; height: 35px;
    border: 1.5px solid #d9e6e4; border-radius: 18px;
    background: rgba(255,255,255,0.3);
    display: flex; align-items: center; justify-content: center;
    color: var(--pill-text); font-weight: 700; font-size: 19px; letter-spacing: 7px;
  }
  .footer-band { left: 0; top: 880px; width: 718px; height: 120px; }
  .slogan {
    left: 0; top: 937px; width: 740px; text-align: center;
    color: var(--white); font-weight: 700; font-style: italic;
    font-variant: small-caps; font-size: 32px; letter-spacing: 1px;
  }
</style>
</head>
<body>
  <main class="poster">
    <div class="hero-photo" role="img" aria-label="Sunlit golf fairway with a golf ball resting beside an iron club head"></div>

    <svg class="frame" viewBox="0 0 718 1000" aria-hidden="true">
      <g stroke="#ffffff" stroke-width="3" fill="none">
        <line x1="25" y1="23" x2="693" y2="23"/>
        <line x1="44" y1="160" x2="44" y2="870"/>
        <line x1="676" y1="23" x2="676" y2="910"/>
      </g>
    </svg>

    <svg class="brand-tab" viewBox="0 0 207 161" aria-hidden="true">
      <path d="M0 0H207V146Q207 161 190 154Q110 120 40 150Q0 166 0 140Z" fill="#0a5f5b"/>
    </svg>
    <div class="brand-name">Fairway Tally</div>

    <h2 class="values-title">Our Key Values:</h2>
    <ul class="values-list">
      <li>Quick and easy</li>
      <li>Formal and polite</li>
      <li>Fun with professional boundary</li>
      <li>Mate-ship relationships</li>
      <li>100% online digital</li>
    </ul>

    <svg class="offer-panel" viewBox="0 0 350 179" aria-hidden="true">
      <path d="M22 0H350V179H110Q90 179 80 162L6 26Q-4 0 22 0Z" fill="#7aa23a"/>
    </svg>
    <p class="offer-text">We provide<br>online payments<br>for golfing services<br>via our website</p>

    <svg class="steps-panel" viewBox="0 0 712 187" aria-hidden="true">
      <path d="M0 0H628Q650 0 638 20L560 165Q548 187 520 187H0Z" fill="#f1f3f2"/>
      <path d="M657 44H712V170H606Q600 170 604 163L648 56Q652 44 657 44Z" fill="#ffffff" opacity="0.35"/>
    </svg>
    <div class="phone-mockup" role="img" aria-label="Mobile phone showing the Fairway Tally payment home screen"></div>

    <h3 class="steps-title">To pay online, just follow three steps:</h3>
    <ol class="steps-list">
      <li><span class="num">1.</span>Visit fairwaytally.com.au</li>
      <li><span class="num">2.</span>Select club</li>
      <li><span class="num">3.</span>Confirm payment</li>
    </ol>

    <div class="url-pill">fairwaytally.com.au</div>

    <svg class="footer-band" viewBox="0 0 718 120" aria-hidden="true">
      <polygon points="0,8 718,45 718,120 0,120" fill="#7aa23a"/>
      <polygon points="340,18 718,8 718,45" fill="#f1f3f2"/>
    </svg>
    <p class="slogan">No Cash-No Worries</p>
  </main>
</body>
</html>
```